Web Design Project

Psychotherapy and Counselling Practice needs a landing page web design.

My business "Larkspur Advisory" specialises in the treatment of Anxiety and Depression with a holistic approach, endeavouring to unlock the key that holds us to ransom in a life that is imbalanced, frustrating, and ultimately of our own making due to our own perceptions and behaviours.

There is much that impacts us which we cannot change, but we are always in control of how we think, and how we frame our experiences.....learning to challenge those thoughts and behaviours that are destructive and disempowering opens up a world of joyful possibility. Life is about making choices, learn to make wiser and healthier choices.......

Larkspur Advisory has a client base of individual clients but will seek to expand to offer services to the Corporate world by offering an adjunct to employers for established "Wellness Programs".

Larkspur Advisory is a highly professional, ethically bound business, with the needs of the client at the forefront of all we do.

Larkspur Advisory wishes to avoid the usual "jargon driven" psychobabble offered on many counselling web pages. It aims to be stylishly presented, clean in look and with as few "words" as possible and a largely white background (faster loading and more powerful impact of what is stated), those words contained in the webpage should be meaningful, persuasive and have an impact simply at glance. Larkspur does not want , or expect, those prospective clients in need of support , to be reading through volumes of industry driven cliches.

At this point Larkspur is just looking for a high quality landing page. However in time this will likely expand to include other sections such as case studies, video content etc.

Target Market(s)

Those in need of emotional support, suffering mental health issues, and those simply wanting to become self aware supported by a mindful therapist.

Industry/Entity Type

Industry

Requirements
Must have
• The design must incorporate the Larkspur logo and colour schemes found on the attached files.

```html
<!DOCTYPE html>
<html lang="en">
<head>
<meta charset="utf-8">
<title>Larkspur Advisory</title>
<link href="https://fonts.googleapis.com/css2?family=Oswald:wght@200;300&family=Open+Sans:wght@400;600;700&family=Questrial&display=swap" rel="stylesheet">
<style>
  :root {
    --green: #8eab0f;
    --green-soft: #cfdca0;
    --grey: #737373;
    --grey-dark: #6b6b6b;
    --grey-light: #9a9a9a;
    --white: #ffffff;
    --icon: #3a3a3a;
  }
  * { margin: 0; padding: 0; box-sizing: border-box; }
  html, body { width: 1200px; height: 1000px; overflow: hidden; background: var(--white); }
  body { position: relative; font-family: "Open Sans", sans-serif; color: var(--grey); }

  .main-nav {
    position: absolute; top: 77px; right: 120px;
    display: flex; align-items: center;
    font-family: "Questrial", sans-serif; font-size: 15px;
  }
  .main-nav a {
    display: block; height: 28px; line-height: 28px; padding: 0 12px;
    margin-left: 15px; color: var(--green); text-decoration: none; border-radius: 5px;
  }
  .main-nav a:last-child { padding-right: 0; }
  .main-nav a.is-active { background: var(--grey); color: var(--white); }
  .nav-rule { position: absolute; top: 116px; left: 120px; width: 960px; height: 1px; background: var(--green-soft); }

  .brand { position: absolute; left: 118px; top: 130px; width: 402px; height: 590px; }
  .brand-vine {
    position: absolute; left: 140px; top: 0; width: 86px; height: 590px;
    background: linear-gradient(180deg, rgba(142,171,15,.25), rgba(142,171,15,.55));
    border-radius: 40px 40px 0 0;
  }
  .brand-name {
    position: absolute; left: 0; top: 176px; width: 402px;
    font-family: "Questrial", sans-serif; font-size: 70px; letter-spacing: 2px;
    line-height: 80px; color: var(--grey); text-align: center;
  }

  .quote {
    position: absolute; left: 565px; top: 162px; width: 480px;
    font-family: "Oswald", sans-serif; font-weight: 200; font-size: 42px;
    letter-spacing: -0.5px; line-height: 47px; white-space: nowrap;
    text-transform: uppercase; color: var(--grey); text-align: center;
    transform: scaleY(1.3); transform-origin: top center;
  }
  .quote em { font-style: normal; color: var(--green); }
  .quote-credit {
    position: absolute; left: 765px; top: 358px; width: 194px; height: 40px;
    background: var(--green); border-radius: 5px; color: var(--white);
    font-family: "Oswald", sans-serif; font-weight: 300; font-size: 17px;
    letter-spacing: 1px; line-height: 40px; text-align: center; text-transform: uppercase;
  }
  .quote-credit::before {
    content: ""; position: absolute; left: 19px; top: -16px;
    border-left: 16px solid var(--green); border-top: 16px solid transparent;
  }

  .contact { position: absolute; left: 615px; top: 488px; width: 411px; text-align: center; }
  .contact-tagline { font-size: 23px; letter-spacing: .5px; height: 46px; color: var(--grey); }
  .contact-tagline strong { color: var(--green); font-weight: 600; }
  .rule { height: 1px; background: var(--green-soft); }
  .contact-call { margin-top: 11px; font-size: 17px; line-height: 22px; color: var(--green); }
  .contact-name { margin-top: 14px; font-size: 24px; font-weight: 700; color: var(--grey); letter-spacing: .5px; line-height: 28px; }
  .contact-cred { font-size: 11px; line-height: 16px; color: var(--grey-light); }
  .contact-line { font-size: 14px; color: var(--grey-dark); line-height: 22px; }
  .contact-line.mobile { margin-top: 15px; }
  .contact .rule.bottom { margin-top: 9px; }

  .site-footer { position: absolute; left: 0; top: 700px; width: 1200px; height: 127px; }
  .site-footer svg.wave { position: absolute; left: 0; top: 0; }
  .social { position: absolute; left: 137px; top: 50px; display: flex; gap: 13px; }
  .social span { width: 35px; height: 35px; border-radius: 50%; background: var(--icon); border: 2px solid #555; display: block; }
  .copyright { position: absolute; left: 138px; top: 100px; font-size: 11px; color: var(--white); letter-spacing: .3px; }
  .site-url { position: absolute; left: 662px; top: 62px; font-family: "Questrial", sans-serif; font-size: 15px; color: var(--green); }
  .site-url strong { font-weight: 400; font-size: 23px; }
</style>
</head>
<body>
  <nav class="main-nav">
    <a class="is-active" href="#">HOME</a>
    <a href="#">OUR SERVICES</a>
    <a href="#">CASE STUDY</a>
    <a href="#">WHO WE ARE</a>
    <a href="#">CONTACT US</a>
  </nav>
  <div class="nav-rule"></div>

  <div class="brand">
    <div class="brand-vine" role="img" aria-label="Climbing green vine illustration"></div>
    <div class="brand-name">LARKSPUR</div>
  </div>

  <blockquote class="quote">
    Just <em>living</em> is not enough. One<br>
    <em>must have sunshine</em>, <em>freedom</em>,<br>
    and <em>a little flower.</em>
  </blockquote>
  <div class="quote-credit">Elin Marsh</div>

  <section class="contact">
    <p class="contact-tagline"><strong>Consulting</strong> is highly Professional</p>
    <div class="rule"></div>
    <p class="contact-call">Call Us Today:</p>
    <p class="contact-name">MARA ELLISON</p>
    <p class="contact-cred">BA (Psych) BSc (Hons) Psych MBPS</p>
    <p class="contact-line mobile">Mobile: 0400 123 987</p>
    <p class="contact-line">E-mail: mara.ellison@larkspurmail.com</p>
    <div class="rule bottom"></div>
  </section>

  <footer class="site-footer">
    <svg class="wave" width="1200" height="127" viewBox="0 0 1200 127">
      <path d="M0 8 C150 2 300 10 400 18 C600 26 900 16 1200 9 L1200 127 L0 127 Z" fill="var(--green)"/>
      <path d="M0 32 C200 30 350 34 500 36 C700 38 950 30 1200 27 L1200 127 L0 127 Z" fill="var(--grey)"/>
    </svg>
    <div class="social"><span></span><span></span><span></span><span></span></div>
    <p class="copyright">Copyright © 2013 LARKSPUR - All rights reserved</p>
    <p class="site-url">www.<strong>larkspuradvisory</strong>.com.au</p>
  </footer>
</body>
</html>
```